Our companies name is The Gilded Ladle and we specialize in craft cupcakes, what I mean by that is that we bake our cupcakes with craft beer and other alcoholic drinks. We are trying to focus on being elegant but at the same time unpretentious. Since we are incorporating beer in our cupcakes we want the business card to have our logo in the front and our information in the back.

Once we select the best design we will provide the contact information to be added. Thank you.

Industry/Entity Type

Business

Font styles to use
Decorative
Script

Requirements
Must have
• Round corners
Should not have
• Square corners

```html
<!DOCTYPE html>
<html lang="en">
<head>
<meta charset="utf-8">
<title>The Gilded Ladle – Business Card</title>
<link rel="stylesheet" href="https://fonts.googleapis.com/css2?family=Archivo:wdth,wght@112,800&display=swap">
<style>
  :root {
    --paper: #ffffff;
    --can-light: #e4e4e4;
    --can-dark: #a9a9a9;
    --rim: #bdbdbd;
    --teal: #7fd3c8;
  }
  html, body {
    margin: 0;
    width: 1200px;
    height: 939px;
    overflow: hidden;
    background: var(--paper);
  }
  .card-sheet { display: block; width: 1200px; height: 939px; }
  .can-body { fill: url(#canShade); }
  .can-rim { fill: var(--rim); }
  .can-lid { fill: var(--can-light); stroke: var(--can-dark); stroke-width: 3; }
  .can-base { fill: var(--can-dark); }
  .label-band { fill: url(#bandShade); }
  .brand-name, .tagline, .contact-name, .contact-line {
    font-family: "Archivo", "Arial Black", sans-serif;
    font-weight: 800;
    font-stretch: 112%;
    fill: var(--teal);
    text-anchor: middle;
  }
  .brand-name { font-size: 36px; letter-spacing: 1px; }
  .tagline, .contact-name { font-size: 30px; letter-spacing: 1px; }
  .contact-line { font-size: 21px; }
</style>
</head>
<body>
<svg class="card-sheet" viewBox="0 0 1200 939" xmlns="http://www.w3.org/2000/svg">
  <defs>
    <linearGradient id="canShade" x1="0" x2="1" y1="0" y2="0">
      <stop offset="0" stop-color="#d6d6d6"/>
      <stop offset="0.12" stop-color="#e6e6e6"/>
      <stop offset="0.55" stop-color="#cfcfcf"/>
      <stop offset="0.88" stop-color="#c4c4c4"/>
      <stop offset="1" stop-color="#a8a8a8"/>
    </linearGradient>
    <linearGradient id="bandShade" x1="0" x2="1" y1="0" y2="0">
      <stop offset="0" stop-color="#b02e38"/>
      <stop offset="0.12" stop-color="#8e1d22"/>
      <stop offset="0.85" stop-color="#7f1a1f"/>
      <stop offset="1" stop-color="#5f1216"/>
    </linearGradient>
    <g id="canShape">
      <path class="can-body" d="M120 66 L505 66 L570 150 L570 800 L515 880 L110 880 L55 800 L55 150 Z"/>
      <ellipse class="can-base" cx="312" cy="880" rx="202" ry="14"/>
      <ellipse class="can-rim" cx="312" cy="64" rx="196" ry="26"/>
      <ellipse class="can-lid" cx="312" cy="62" rx="170" ry="18"/>
      <path class="label-band" d="M55 365 L155 365 C165 318 232 294 312 294 C392 294 460 318 470 365 L570 365 L570 730 C400 722 220 722 55 708 Z"/>
    </g>
  </defs>

  <g class="card-front">
    <use href="#canShape"/>
    <text class="brand-name" x="312" y="455">THE GILDED</text>
    <text class="brand-name" x="312" y="500">LADLE</text>
    <text class="tagline" x="312" y="645">WE SPECIALIZE IN</text>
    <text class="tagline" x="312" y="692">CRAFT CUPCAKES</text>
  </g>

  <g class="card-back" transform="translate(570 0)">
    <use href="#canShape"/>
    <text class="brand-name" x="312" y="455">THE GILDED</text>
    <text class="brand-name" x="312" y="500">LADLE</text>
    <text class="contact-name" x="312" y="634">DANA REYES</text>
    <text class="contact-line" x="312" y="666">E: hello@gildedladlebakery.com</text>
    <text class="contact-line" x="312" y="710">T: 909-555-0142</text>
  </g>
</svg>
</body>
</html>
```